Vormsted Off-Grid Energy

The company provides world wide installations and products for off-grid energy solutions. This means AC power where there is no network available. Mostly this is with solar panels combined with hybrid inverters and Lithium batteries. In the future small windmills and hydropower. The company is Dutch but has a hub in Hungary to supply the Balkan and surrounding countries.

We sell all Koru products and also Pinewatt and Lumask energy products

I have 3 versions of my logo. 2 attached and the third is the Off-grid energy text in black. Just see what works best with the design.
Obviously I need a good design but also good coding. It needs to meet al the latest (Google) search engine standards and should heave a web shop.
The web shop should be able to work with different currencies and calculate international shipping fees. Orders should be paid with; credit card, Quidflow, Fenpay or whatever is used internationally.

Coding

Number of Pages Required

5+ page

Font styles to use
Other font styles liked:
• see logo

Colors
0054AA
0677BA
7BADD7
CADEEF
E8F1F8
0094D4
00A9DD
6FCCEA
C7EBF8
E9F6FB
59FF00
82FF00
B8FF75
E3FFCB
F4FFEA
EB3D1F
EC4F4E
F09395
F8D3D4
FCEDEE

Requirements
Must have
• web shop
Nice to have
• slick design
Should not have
• stupid things ;-)

```html
<!DOCTYPE html>
<html lang="en">
<head>
<meta charset="utf-8">
<title>Vormsted Off-Grid Energy – Supervision &amp; control for solar power plants</title>
<link href="https://fonts.googleapis.com/css2?family=Lexend:wght@400;500;600&family=Jost:wght@400;500;600&display=swap" rel="stylesheet">
<style>
:root{
  --accent:#EB3D1F;
  --accent-soft:#EC4F4E;
  --lime:#82FF00;
  --lime-soft:#B8FF75;
  --dark:#1d2228;
  --darker:#15191e;
  --ink:#1b1b1b;
  --muted:#555b62;
  --line:#d9dde2;
  --white:#ffffff;
  --sky:#6fa3d6;
  --panel:#1f4f8f;
}
*{box-sizing:border-box;margin:0;padding:0}
html,body{width:1200px;height:5168px;overflow:hidden}
body{position:relative;font-family:"Jost",sans-serif;color:var(--ink);background:var(--white)}
h1,h2,h3,h4{font-family:"Lexend",sans-serif;font-weight:500}
.abs{position:absolute}
.photo{position:absolute;overflow:hidden}
.btn{position:absolute;display:flex;align-items:center;justify-content:center;gap:8px;font-size:12px;font-weight:500;border-radius:2px;color:var(--white);background:var(--accent);text-decoration:none}
.btn.lime{background:var(--lime);color:var(--ink)}
.btn svg{width:12px;height:12px}
.eyebrow{position:absolute;font-size:13px;letter-spacing:2.5px;color:var(--accent);display:flex;align-items:center;gap:12px}
.eyebrow.center{left:0;width:1200px;justify-content:center}
.eyebrow .rule{display:inline-block;width:36px;height:1px;background:var(--accent)}
.title{position:absolute;left:0;width:1200px;text-align:center;font-size:39px}
.on-dark{color:var(--white)}
/* top bar + nav */
.topbar{top:0;left:0;width:1200px;height:28px;background:var(--darker);color:#ddd;font-size:9px;display:flex;align-items:center;padding:0 100px;gap:22px}
.topbar .socials{margin-left:auto;display:flex;gap:6px}
.topbar .socials span{width:14px;height:14px;border-radius:50%;border:1px solid #bbb}
.nav{top:28px;left:0;width:1200px;height:72px;background:var(--white);display:flex;align-items:center;padding:0 100px}
.brand{display:flex;align-items:center;gap:8px;font-family:"Lexend",sans-serif;font-weight:600;font-size:18px;color:var(--ink)}
.brand .mark{width:14px;height:14px;background:var(--accent)}
.brand small{display:block;font-size:8px;font-weight:600;letter-spacing:1.5px;color:var(--ink)}
.menu{display:flex;gap:34px;margin-left:auto;margin-right:24px;font-size:12px;list-style:none}
.menu li:first-child{color:var(--accent)}
.nav .search{width:16px;height:16px;margin-right:22px}
.nav .quote{position:static;width:124px;height:32px}
/* hero */
.hero{top:100px;left:0;width:1200px;height:590px;background:linear-gradient(100deg,#123 0%,#2a4a70 30%,#5a8fc4 60%,#9cc3e6 100%)}
.hero .shade{position:absolute;inset:0;background:linear-gradient(90deg,rgba(10,15,25,.7),rgba(10,15,25,.1) 60%)}
.hero h1{position:absolute;left:100px;top:160px;font-size:47px;line-height:1.07;color:var(--white);width:520px}
.hero p{position:absolute;left:100px;top:328px;font-size:12.5px;line-height:1.6;color:#eee;width:400px}
.edge{position:absolute;left:0;width:1200px}
/* products */
.card{position:absolute;background:var(--white);box-shadow:0 4px 18px rgba(0,0,0,.08)}
.product{top:806px;width:238px;height:256px}
.product .photo{left:0;top:0;width:238px;height:138px}
.product .body{position:absolute;left:8px;right:8px;top:132px;background:var(--white);padding:12px 14px}
.product h3{font-size:16px;margin-bottom:10px}
.tick{display:flex;gap:8px;font-size:10.5px;line-height:1.45;color:var(--muted)}
.tick svg{flex:none;width:10px;height:10px;margin-top:3px}
.more{display:inline-flex;align-items:center;gap:6px;margin-top:12px;font-size:11px;color:var(--accent)}
.more svg{width:10px;height:10px}
/* dark sections */
.dark{position:absolute;left:0;width:1200px;background:linear-gradient(180deg,#20262d,#171b20)}
.about h2{position:absolute;left:608px;top:1318px;font-size:39px;line-height:1.15;color:var(--white)}
.about .copy{position:absolute;left:608px;top:1432px;width:492px;font-size:11.5px;line-height:1.55;color:#d6d8db}
.about .copy p{margin-bottom:10px}
/* why choose */
.feature{position:absolute;width:260px}
.feature h4{font-size:17px;margin-bottom:6px;font-weight:500}
.feature.right-al{text-align:right}
.feature .tick{font-size:11px}
.feature.right-al .tick{justify-content:flex-end;text-align:right}
.bubble{position:absolute;width:58px;height:58px;border-radius:50%;background:var(--dark);border:2px solid var(--accent);display:flex;align-items:center;justify-content:center}
.bubble svg{width:28px;height:28px}
.centerlogo{position:absolute;left:470px;top:1950px;width:260px;text-align:center;font-family:"Lexend",sans-serif;font-weight:600;font-size:34px;color:var(--ink)}
.centerlogo small{display:block;font-size:12px;letter-spacing:2px}
/* webshop */
.shop h2{position:absolute;left:108px;top:2382px;font-size:40px;line-height:1.15;color:var(--white)}
.shop ul{position:absolute;left:108px;top:2494px;list-style:none;font-size:13px;line-height:1.7;color:#e6e6e6}
.shop li::before{content:"· ";color:#aaa}
/* projects */
.project{position:absolute;top:2916px;width:238px;height:302px}
.project .label{position:absolute;left:26px;bottom:32px;font-family:"Lexend",sans-serif;font-size:16px;color:var(--white)}
.arrows{position:absolute;left:38px;top:3036px}
/* news */
.news{top:3524px;width:320px;height:332px;border:2px solid var(--accent);background:var(--white)}
.news .photo{left:0;top:0;width:276px;height:172px}
.news .date{position:absolute;right:6px;top:20px;writing-mode:vertical-rl;transform:rotate(180deg);font-family:"Lexend",sans-serif;font-size:14px;color:var(--accent)}
.news .body{position:absolute;left:12px;top:182px;right:12px}
.news .by{font-size:9px;color:var(--muted);margin-bottom:4px}
.news h3{font-size:16px;line-height:1.35;margin-bottom:6px}
.news p{font-size:11px;line-height:1.45;color:var(--muted)}
/* contact */
.contact h2{position:absolute;left:626px;top:4104px;font-size:39px}
.field{position:absolute;border:1px solid #c9cdd2;border-radius:3px;font-size:9px;color:#999;padding:9px 12px}
/* footer */
.footer{top:4500px;height:668px}
.footer .logo{position:absolute;left:0;width:1200px;top:4688px;text-align:center;font-family:"Lexend",sans-serif;font-weight:600;font-size:40px;color:var(--white)}
.footer .logo small{display:block;font-size:14px;letter-spacing:3px}
.info{position:absolute;top:4872px;height:142px;border:1px solid #3b4148;text-align:center;color:var(--white)}
.info .ico{width:46px;height:46px;border-radius:50%;background:var(--accent);margin:16px auto 18px;display:flex;align-items:center;justify-content:center}
.info .ico svg{width:20px;height:20px}
.info strong{display:block;font-weight:400;font-size:18px}
.info span{display:block;margin-top:8px;font-size:13px;color:#d0d0d0}
.footnav{position:absolute;left:0;width:1200px;top:5040px;height:52px;border-top:1px solid #3b4148;border-bottom:1px solid #3b4148;display:flex;justify-content:space-around;align-items:center;list-style:none;color:var(--white);font-size:13px;padding:0 80px}
.copyright{position:absolute;left:0;width:1200px;top:5124px;text-align:center;color:#cfcfcf;font-size:13px;letter-spacing:1px}
</style>
</head>
<body>

<!-- Top bar -->
<div class="abs topbar">
  <span>(123) 555-0147</span>
  <span>info@vormstedoffgrid.com</span>
  <span>Lorem Ipsum is simply dummy text of the printing and typesetting</span>
  <div class="socials"><span></span><span></span><span></span><span></span></div>
</div>

<!-- Navigation -->
<header class="abs nav">
  <div class="brand"><span class="mark"></span><div>Vormsted<small>OFF-GRID ENERGY</small></div></div>
  <ul class="menu"><li>Home</li><li>Products</li><li>Solutions</li><li>Webshop</li><li>About Us</li><li>Resource</li><li>Contact</li></ul>
  <svg class="search" viewBox="0 0 16 16" fill="none" stroke="#222" stroke-width="1.6"><circle cx="7" cy="7" r="5"/><path d="M11 11l4 4"/></svg>
  <a class="btn quote">Get A Quote <svg viewBox="0 0 12 12" fill="none" stroke="currentColor" stroke-width="1.5"><path d="M1 6h9M7 3l3 3-3 3"/></svg></a>
</header>

<!-- Hero -->
<section class="photo hero" role="img" aria-label="Rows of solar panels under a bright sky at sunset">
  <div class="shade"></div>
  <div class="eyebrow" style="left:100px;top:132px">Solar Energy Solutions <span class="rule"></span></div>
  <h1>Supervision &amp; control solutions for solar power plants.</h1>
  <p>Empowering homes and businesses with cutting-edge solar, battery, and inverter technology. Dependable power, anywhere</p>
  <a class="btn" style="left:100px;top:392px;width:174px;height:32px">Explore Our Solutions <svg viewBox="0 0 12 12" fill="none" stroke="currentColor" stroke-width="1.5"><path d="M1 6h9M7 3l3 3-3 3"/></svg></a>
  <svg class="edge" style="bottom:0;height:90px" viewBox="0 0 1200 90" preserveAspectRatio="none">
    <polygon points="0,90 0,40 1200,10 1200,90" fill="#82FF00"/>
    <polygon points="0,90 0,64 600,30 1200,48 1200,90" fill="#EB3D1F"/>
    <polygon points="0,90 0,76 600,44 1200,60 1200,90" fill="#fff"/>
  </svg>
</section>

<!-- Featured products -->
<div class="eyebrow center" style="top:708px"><span class="rule"></span>Our Products<span class="rule"></span></div>
<h2 class="title" style="top:736px">Featured Products</h2>

<article class="card product" style="left:100px">
  <div class="photo" role="img" aria-label="Hybrid inverter cabinet outdoors" style="background:linear-gradient(160deg,#bcd3ea,#e7edf2 55%,#9aa5b0)"></div>
  <div class="body"><h3>Koru Hybrid Inverters</h3>
    <div class="tick"><svg viewBox="0 0 10 10" fill="none" stroke="#EB3D1F" stroke-width="1.6"><path d="M1 5l3 3 5-7"/></svg>Reliable, high-efficiency inverters for seamless solar integration.</div>
    <span class="more">Shop Now <svg viewBox="0 0 12 12" fill="none" stroke="currentColor" stroke-width="1.5"><path d="M1 6h9M7 3l3 3-3 3"/></svg></span></div>
</article>
<article class="card product" style="left:354px">
  <div class="photo" role="img" aria-label="Battery storage containers in a field" style="background:linear-gradient(170deg,#c6dcf0,#eef2f4 50%,#8fa0ad)"></div>
  <div class="body"><h3>Pinewatt Batteries</h3>
    <div class="tick"><svg viewBox="0 0 10 10" fill="none" stroke="#EB3D1F" stroke-width="1.6"><path d="M1 5l3 3 5-7"/></svg>Reliable, high-efficiency inverters for seamless solar integration.</div>
    <span class="more">Shop Now <svg viewBox="0 0 12 12" fill="none" stroke="currentColor" stroke-width="1.5"><path d="M1 6h9M7 3l3 3-3 3"/></svg></span></div>
</article>
<article class="card product" style="left:608px">
  <div class="photo" role="img" aria-label="Energy equipment with blue components" style="background:linear-gradient(160deg,#4a5a6a,#1f4e8a 55%,#2a3440)"></div>
  <div class="body"><h3>Lumask Energy Products</h3>
    <div class="tick"><svg viewBox="0 0 10 10" fill="none" stroke="#EB3D1F" stroke-width="1.6"><path d="M1 5l3 3 5-7"/></svg>Reliable, high-efficiency inverters for seamless solar integration.</div>
    <span class="more">Shop Now <svg viewBox="0 0 12 12" fill="none" stroke="currentColor" stroke-width="1.5"><path d="M1 6h9M7 3l3 3-3 3"/></svg></span></div>
</article>
<article class="card product" style="left:862px">
  <div class="photo" role="img" aria-label="Small wind turbine against a blue sky" style="background:linear-gradient(170deg,#1d64c2,#4f94de 60%,#cfe1f3)"></div>
  <div class="body"><h3>Small Wind Turbines</h3>
    <div class="tick"><svg viewBox="0 0 10 10" fill="none" stroke="#EB3D1F" stroke-width="1.6"><path d="M1 5l3 3 5-7"/></svg>Coming Soon</div>
    <span class="more" style="margin-top:24px">Explore Now <svg viewBox="0 0 12 12" fill="none" stroke="currentColor" stroke-width="1.5"><path d="M1 6h9M7 3l3 3-3 3"/></svg></span></div>
</article>
<a class="btn lime" style="left:528px;top:1098px;width:144px;height:32px">Get A Quote <svg viewBox="0 0 12 12" fill="none" stroke="currentColor" stroke-width="1.5"><path d="M1 6h9M7 3l3 3-3 3"/></svg></a>

<!-- About -->
<section class="dark about" style="top:1150px;height:574px">
  <svg class="edge" style="top:0;height:110px" viewBox="0 0 1200 110" preserveAspectRatio="none">
    <polygon points="0,0 1200,0 1200,60 600,42 0,95" fill="#fff"/>
    <polygon points="0,95 600,42 1200,60 1200,14 0,62" fill="#82FF00" opacity="0"/>
    <polygon points="0,60 600,42 1200,0 1200,20 600,54 0,80" fill="#82FF00"/>
    <polygon points="0,80 600,54 1200,20 1200,34 600,66 0,100" fill="#EB3D1F"/>
  </svg>
</section>
<div class="photo" role="img" aria-label="Solar panel array on a tracker under blue sky" style="left:100px;top:1302px;width:304px;height:302px;background:linear-gradient(170deg,#a9cbeb,#4a78b0 55%,#3a4a58)"></div>
<div class="photo" role="img" aria-label="Engineer in hard hat checking solar panels with a tablet" style="left:328px;top:1358px;width:252px;height:294px;border:6px solid #fff;background:linear-gradient(160deg,#3c72b6,#6fa0d4 50%,#d88a2a 80%,#3b5d8c)"></div>
<div class="eyebrow" style="left:608px;top:1296px">Who We Are <span class="rule"></span></div>
<h2 class="about">
</h2>
<h2 class="abs" style="left:608px;top:1318px;font-size:39px;line-height:1.17;color:#fff">About Vormsted<br>off Grid Energy</h2>
<div class="about"><div class="copy">
  <p>Vormsted Off-Grid Energy is a global provider of reliable, sustainable off-grid energy solutions. We specialize in advanced solar, battery, and inverter technologies to power homes, businesses, and remote locations worldwide.</p>
  <p>To deliver high-quality, efficient, and cost-effective energy solutions that empower individuals and businesses to achieve energy independence. A future where clean, renewable energy is accessible to all, eliminating dependence on traditional power grids and fostering sustainable growth.</p>
  <p>Headquartered in the Netherlands with a distribution hub in Hungary, allowing us to efficiently serve customers across Europe and beyond.</p>
</div></div>
<a class="btn" style="left:608px;top:1630px;width:176px;height:32px">Learn More About Us <svg viewBox="0 0 12 12" fill="none" stroke="currentColor" stroke-width="1.5"><path d="M1 6h9M7 3l3 3-3 3"/></svg></a>

<!-- Why choose -->
<div class="eyebrow center" style="top:1776px"><span class="rule"></span>Why Us<span class="rule"></span></div>
<h2 class="title" style="top:1806px">Why Choose Vormsted</h2>
<svg class="abs" style="left:400px;top:1950px" width="400" height="160" viewBox="0 0 400 160" fill="none" stroke="#EB3D1F" stroke-width="2" stroke-dasharray="8 7"><path d="M20 10 Q200 260 380 10"/></svg>
<div class="centerlogo"><span style="display:inline-block;width:18px;height:18px;background:var(--lime);margin-right:8px;vertical-align:middle"></span>Vormsted<small style="color:var(--accent)">OFF GRID ENERGY</small></div>

<div class="feature right-al" style="left:104px;top:1910px"><h4>Global Expertise</h4><div class="tick"><svg viewBox="0 0 10 10" fill="none" stroke="#EB3D1F" stroke-width="1.6"><path d="M1 5l3 3 5-7"/></svg>Worldwide installations with hubs<br>in the Netherlands and Hungary</div></div>
<div class="bubble" style="left:378px;top:1898px"><svg viewBox="0 0 28 28" fill="none" stroke="#EB3D1F" stroke-width="1.6"><circle cx="14" cy="14" r="10"/><path d="M4 14h20M14 4c4 4 4 16 0 20M14 4c-4 4-4 16 0 20"/></svg></div>

<div class="bubble" style="left:760px;top:1890px"><svg viewBox="0 0 28 28" fill="none" stroke="#82FF00" stroke-width="1.6"><path d="M6 22C6 12 12 6 22 6c0 10-6 16-16 16zM6 22l9-9"/></svg></div>
<div class="feature" style="left:834px;top:1902px;width:280px"><h4>Sustainable &amp; Cost-Effective</h4><div class="tick" style="padding-left:4px"><svg viewBox="0 0 10 10" fill="none" stroke="#EB3D1F" stroke-width="1.6"><path d="M1 5l3 3 5-7"/></svg>Worldwide installations with hubs<br>in the Netherlands and Hungary</div></div>

<div class="feature right-al" style="left:164px;top:2050px"><h4>Reliable &amp; Efficient</h4><div class="tick"><svg viewBox="0 0 10 10" fill="none" stroke="#EB3D1F" stroke-width="1.6"><path d="M1 5l3 3 5-7"/></svg>High-performance solar panels,<br>batteries, and inverters</div></div>
<div class="bubble" style="left:452px;top:2036px"><svg viewBox="0 0 28 28" fill="none" stroke="#82FF00" stroke-width="1.6"><rect x="7" y="7" width="14" height="14" rx="2"/><path d="M11 3v4M17 3v4M11 21v4M17 21v4M3 11h4M3 17h4M21 11h4M21 17h4"/></svg></div>

<div class="bubble" style="left:690px;top:2036px"><svg viewBox="0 0 28 28" fill="none" stroke="#EB3D1F" stroke-width="1.6"><circle cx="14" cy="14" r="4"/><path d="M14 3v4M14 21v4M3 14h4M21 14h4M6 6l3 3M19 19l3 3M6 22l3-3M19 9l3-3"/></svg></div>
<div class="feature" style="left:772px;top:2050px"><h4>Custom Solutions</h4><div class="tick"><svg viewBox="0 0 10 10" fill="none" stroke="#EB3D1F" stroke-width="1.6"><path d="M1 5l3 3 5-7"/></svg>High-performance solar panels,<br>batteries, and inverters</div></div>

<!-- Webshop -->
<section class="dark shop" style="top:2176px;height:574px">
  <div class="photo" role="img" aria-label="Two engineers in hard hats surveying a solar farm" style="left:0;top:0;width:1200px;height:574px;clip-path:polygon(680px 40px,1200px 40px,1200px 574px,440px 574px);background:linear-gradient(150deg,#d7e2ec,#7aa0c8 35%,#2c5690 70%,#1d2f4a)"></div>
  <svg class="edge" style="top:0;height:574px" viewBox="0 0 1200 574" preserveAspectRatio="none">
    <polygon points="0,0 1200,0 1200,10 0,50" fill="#fff"/>
    <polygon points="0,0 0,18 1200,58 1200,28 620,20" fill="#82FF00"/>
    <polygon points="0,18 0,26 600,48 1200,70 1200,58" fill="#EB3D1F"/>
    <polygon points="0,0 0,14 1200,50 1200,20 600,14" fill="#fff" opacity="0"/>
    <polygon points="676,40 690,40 452,574 438,574" fill="#82FF00"/>
  </svg>
</section>
<div class="eyebrow" style="left:108px;top:2356px">Visit Our Webshop <span class="rule"></span></div>
<div class="shop">
  <h2>HOw We Create<br>Solar Enargy ?</h2>
  <ul><li>Multi-currency support (EUR, USD, HUF, etc.)</li><li>International Shipping Calculator</li><li>Payment Options: Credit Card, Quidflow, Fenpay</li></ul>
</div>
<a class="btn" style="left:108px;top:2586px;width:176px;height:32px">Browse Our Products <svg viewBox="0 0 12 12" fill="none" stroke="currentColor" stroke-width="1.5"><path d="M1 6h9M7 3l3 3-3 3"/></svg></a>

<!-- Projects -->
<div class="eyebrow center" style="top:2816px"><span class="rule"></span>Our Project<span class="rule"></span></div>
<h2 class="title" style="top:2846px">Success Stories &amp; Installations</h2>
<svg class="arrows" width="36" height="56" viewBox="0 0 36 56" fill="none" stroke="#222" stroke-width="2"><path d="M4 10h28M24 2l8 8-8 8M32 46H4M12 38l-8 8 8 8"/></svg>
<div class="project photo" role="img" aria-label="Engineers beside a wind turbine and solar field" style="left:100px;background:linear-gradient(180deg,#9dbbd8,#55789c 55%,#1e2a38)"><span class="label">Lorem Ipsum is simply</span></div>
<div class="project photo" role="img" aria-label="Aerial view of solar rows on grass" style="left:354px;background:linear-gradient(180deg,#3d4a35,#566b45 45%,#2b3a52 80%,#1a1f27)"><span class="label">Lorem Ipsum is simply</span></div>
<div class="project photo" role="img" aria-label="Wind turbine on a hill above solar panels" style="left:608px;background:linear-gradient(180deg,#8fb3d6,#6a8da8 45%,#2a4f86 75%,#18212d)"><span class="label">Lorem Ipsum is simply</span></div>
<div class="project photo" role="img" aria-label="Two engineers walking through solar panels" style="left:862px;background:linear-gradient(180deg,#a8c6e3,#5a86b8 50%,#2a4a7a 75%,#171d26)"><span class="label">Lorem Ipsum is simply</span></div>
<div class="project photo" role="img" aria-label="Solar panels at dusk" style="left:1116px;width:84px;background:linear-gradient(180deg,#7aa8d8,#2f5c97 60%,#171d26)"><span class="label">Lorem</span></div>
<a class="btn lime" style="left:528px;top:3240px;width:144px;height:32px">Get A Quote <svg viewBox="0 0 12 12" fill="none" stroke="currentColor" stroke-width="1.5"><path d="M1 6h9M7 3l3 3-3 3"/></svg></a>

<!-- News -->
<section class="dark" style="top:3290px;height:694px">
  <svg class="edge" style="top:0;height:80px" viewBox="0 0 1200 80" preserveAspectRatio="none">
    <polygon points="0,0 1200,0 1200,40 0,20" fill="#fff"/>
    <polygon points="0,10 600,30 1200,40 1200,52 600,44 0,30" fill="#82FF00"/>
    <polygon points="0,30 600,44 1200,52 1200,62 600,54 0,40" fill="#EB3D1F"/>
  </svg>
</section>
<div class="eyebrow center" style="top:3424px"><span class="rule"></span>Latest News &amp; Bolg<span class="rule"></span></div>
<h2 class="title on-dark" style="top:3454px">News &amp; Articals</h2>

<article class="card news" style="left:100px">
  <div class="photo" role="img" aria-label="Engineer with hard hat in front of solar panels and a wind turbine" style="background:linear-gradient(170deg,#a7c7e6,#5d8fc4 50%,#c9a43a 80%,#2c4c7a)"></div>
  <span class="date">February5, 2025</span>
  <div class="body"><div class="by">By Mara Velden</div><h3>Powering Pacific's Energy<br>Powering Transition</h3><p>Vormsted Off-Grid Energy is a global provider of reliable, sustainable off-grid</p><span class="more">Learn More <svg viewBox="0 0 12 12" fill="none" stroke="currentColor" stroke-width="1.5"><path d="M1 6h9M7 3l3 3-3 3"/></svg></span></div>
</article>
<article class="card news" style="left:440px">
  <div class="photo" role="img" aria-label="Solar farm at sunset" style="background:linear-gradient(180deg,#3a5a8a,#e08a3a 40%,#f3c66a 50%,#2a5a9a 75%,#1b2f55)"></div>
  <span class="date">February5, 2025</span>
  <div class="body"><div class="by">By Mara Velden</div><h3>Powering Pacific's Energy<br>Powering Transition</h3><p>Vormsted Off-Grid Energy is a global provider of reliable, sustainable off-grid</p><span class="more">Learn More <svg viewBox="0 0 12 12" fill="none" stroke="currentColor" stroke-width="1.5"><path d="M1 6h9M7 3l3 3-3 3"/></svg></span></div>
</article>
<article class="card news" style="left:780px">
  <div class="photo" role="img" aria-label="Solar panel tracker on grassland" style="background:linear-gradient(170deg,#b7d0e8,#5b86bb 50%,#30506e 80%,#5b7240)"></div>
  <span class="date">February5, 2025</span>
  <div class="body"><div class="by">By Mara Velden</div><h3>Powering Pacific's Energy<br>Powering Transition</h3><p>Vormsted Off-Grid Energy is a global provider of reliable, sustainable off-grid</p><span class="more">Learn More <svg viewBox="0 0 12 12" fill="none" stroke="currentColor" stroke-width="1.5"><path d="M1 6h9M7 3l3 3-3 3"/></svg></span></div>
</article>
<a class="btn" style="left:514px;top:3896px;width:174px;height:32px">Explore Our News <svg viewBox="0 0 12 12" fill="none" stroke="currentColor" stroke-width="1.5"><path d="M1 6h9M7 3l3 3-3 3"/></svg></a>

<!-- Contact -->
<div class="photo" role="img" aria-label="Engineer in hard hat and safety vest holding a device near solar panels" style="left:100px;top:4044px;width:440px;height:426px;background:linear-gradient(150deg,#b5cfe8,#4f83c0 45%,#d7d04a 70%,#2a4c7c)"></div>
<div class="eyebrow" style="left:626px;top:4072px">Get In Touch <span class="rule"></span></div>
<section class="contact">
  <h2>Contact Us</h2>
  <div class="field" style="left:626px;top:4158px;width:228px;height:34px">First Name</div>
  <div class="field" style="left:872px;top:4158px;width:228px;height:34px">Last Name</div>
  <div class="field" style="left:626px;top:4208px;width:228px;height:34px">Email</div>
  <div class="field" style="left:872px;top:4208px;width:228px;height:34px">Phone</div>
  <div class="field" style="left:626px;top:4258px;width:474px;height:120px">Message</div>
  <a class="btn" style="left:626px;top:4410px;width:120px;height:32px">Submit <svg viewBox="0 0 12 12" fill="none" stroke="currentColor" stroke-width="1.5"><path d="M1 6h9M7 3l3 3-3 3"/></svg></a>
</section>

<!-- Footer -->
<footer class="dark footer">
  <svg class="edge" style="top:0;height:70px" viewBox="0 0 1200 70" preserveAspectRatio="none">
    <polygon points="0,0 1200,0 1200,40 0,10" fill="#fff"/>
    <polygon points="0,10 600,28 1200,40 1200,52 600,40 0,22" fill="#82FF00"/>
    <polygon points="0,22 600,40 1200,52 1200,60 600,50 0,32" fill="#EB3D1F"/>
  </svg>
</footer>
<div class="footer"><div class="logo"><span style="display:inline-block;width:22px;height:22px;background:var(--lime);margin-right:10px;vertical-align:middle"></span>Vormsted<small>OFF GRID ENERGY</small></div></div>
<div class="info" style="left:100px;width:336px"><div class="ico"><svg viewBox="0 0 20 20" fill="none" stroke="#fff" stroke-width="1.6"><path d="M5 2l3 4-2 2c1 2 3 4 5 5l2-2 4 3-2 3C9 17 3 11 2 5z"/></svg></div><strong style="letter-spacing:3px">(123)-555-0147</strong><span>Our Phone</span></div>
<div class="info" style="left:436px;width:328px"><div class="ico"><svg viewBox="0 0 20 20" fill="none" stroke="#fff" stroke-width="1.6"><rect x="2" y="4" width="16" height="12" rx="1"/><path d="M2 5l8 6 8-6"/></svg></div><strong>hello@vormstedoffgrid.com</strong><span>Our Email</span></div>
<div class="info" style="left:796px;width:304px"><div class="ico"><svg viewBox="0 0 20 20" fill="none" stroke="#fff" stroke-width="1.6"><path d="M10 18s6-6 6-10a6 6 0 0 0-12 0c0 4 6 10 6 10z"/><circle cx="10" cy="8" r="2"/></svg></div><strong style="font-size:16px">418 Harbor Lane suite 12 Delft</strong><span>Our Address</span></div>
<ul class="footnav"><li>Home</li><li>Products</li><li>Solutions</li><li>Webshop</li><li>About Us</li><li>Resource</li><li>Contact</li></ul>
<p class="copyright">© Copyright All Right Reserved 2025</p>

</body>
</html>
```